Book Cover - for a Murder book

PROJECT DEADLINE JAN 6TH END OF DAY (Seattle Time).
Goal of the project is to design a book cover for a book related to the investigation of the murder of the Mexican presidential candidate Ramiro Esteban Vallarta.
Look at presidential assassination books in Quillora for ideas.
Also look at pictures in the web of Ramiro Esteban Vallarta, for example here:
http://www.fotobuscador-demo.net/images/search?q=ramiro+esteban+vallarta&FORM=HDRSC2
Must deliver in format that can be modified (either PSD or Illustrator), as well as in PNG.
The author of the book is the most important lawyer in Mexico, so the cover should show that this book is serious, interesting, deep, to be trusted.
Image should contain:
Image: 1563 pixels x 2500 pixels (front page)
- and extend the design to cover the side of the book and the back of the book
Back of the book: a placeholder for a small title, a picture of the author, and a few lines of text
Title of the book: Testigo Nueve
Subtitle (smaller font): El asesinato de Ramiro Esteban Vallarta
Author: Dr. Martín Olvera Quintana
I will also create a version in English, changing the text to:
Title of the Book: Witness Nine
Subtitle (smaller font): The assasination of Ramiro Esteban Vallarta
Hi, we've received many great designs, so we have more than enough. We will be making the decision tomorrow, January 6th, end of day.
Target Market(s)
Serious readers of investigative murders.
Industry/Entity Type
Lawyer
Look and feel

```html
<!DOCTYPE html>
<html lang="es">
<head>
<meta charset="utf-8">
<title>Testigo Nueve — Cubierta y lomo</title>
<link rel="stylesheet" href="https://fonts.googleapis.com/css2?family=Cinzel:wght@400&family=Libre+Baskerville:wght@700&display=swap">
<style>
  :root {
    --page-bg: #f2f2f2;
    --cover-black: #0a0a0b;
    --suit-dark: #17171a;
    --tie-red: #6e1019;
    --tie-deep: #3a0a0f;
    --title-white: #f4f4f4;
    --subtitle-red: #c0141f;
    --spine-black: #070708;
  }
  * { margin: 0; padding: 0; box-sizing: border-box; }
  html, body {
    width: 1070px;
    height: 1200px;
    overflow: hidden;
    background: var(--page-bg);
  }
  .book-jacket {
    position: absolute;
    left: 181px;
    top: 104px;
    width: 708px;
    height: 992px;
    display: flex;
  }

  /* Lomo */
  .book-spine {
    position: relative;
    width: 88px;
    height: 100%;
    background: var(--spine-black);
    border-right: 1px solid #1c1c1f;
  }
  .spine-title {
    position: absolute;
    top: 28px;
    left: 0;
    right: 0;
    text-align: center;
    font-family: "Cinzel", serif;
    color: var(--title-white);
    line-height: 1;
  }
  .spine-title-top { display: block; font-size: 13px; letter-spacing: -0.3px; }
  .spine-title-bottom { display: block; font-size: 24px; margin-top: 2px; }
  .spine-subtitle {
    position: absolute;
    top: 100px;
    left: 50%;
    transform: translateX(-50%);
    writing-mode: vertical-rl;
    font-family: "Cinzel", serif;
    font-size: 15px;
    line-height: 18px;
    color: var(--subtitle-red);
    white-space: nowrap;
  }
  .spine-author {
    position: absolute;
    top: 410px;
    left: 50%;
    transform: translateX(-50%);
    writing-mode: vertical-rl;
    font-family: "Libre Baskerville", serif;
    font-weight: 700;
    font-size: 17px;
    letter-spacing: 0.5px;
    color: var(--title-white);
    white-space: nowrap;
  }

  /* Portada */
  .book-front {
    position: relative;
    width: 620px;
    height: 100%;
    background: var(--cover-black);
    overflow: hidden;
  }
  .cover-photo {
    position: absolute;
    left: 0;
    top: 0;
    width: 100%;
    height: 700px;
    background:
      linear-gradient(to bottom, rgba(10,10,11,0) 0%, rgba(10,10,11,0) 65%, var(--cover-black) 100%),
      linear-gradient(to right,
        var(--suit-dark) 0%,
        #1d1b1d 28%,
        var(--tie-deep) 40%,
        var(--tie-red) 50%,
        var(--tie-deep) 60%,
        #1d1b1d 72%,
        var(--suit-dark) 100%);
  }
  .cover-text {
    position: absolute;
    left: 0;
    right: 0;
    text-align: center;
  }
  .book-title {
    top: 592px;
    font-family: "Cinzel", serif;
    font-weight: 400;
    color: var(--title-white);
    font-size: 80px;
    line-height: 80px;
    letter-spacing: -1px;
  }
  .book-subtitle {
    top: 764px;
    font-family: "Cinzel", serif;
    font-weight: 400;
    color: var(--subtitle-red);
    font-size: 18px;
    letter-spacing: 0.3px;
  }
  .book-author {
    top: 818px;
    font-family: "Libre Baskerville", serif;
    font-weight: 700;
    color: var(--title-white);
    font-size: 20px;
    letter-spacing: 0.5px;
  }
</style>
</head>
<body>
  <div class="book-jacket">
    <aside class="book-spine">
      <p class="spine-title">
        <span class="spine-title-top">TESTIGO</span>
        <span class="spine-title-bottom">NUEVE</span>
      </p>
      <p class="spine-subtitle">EL ASESINATO DE<br>RAMIRO ESTEBAN VALLARTA</p>
      <p class="spine-author">DR. MARTÍN OLVERA QUINTANA</p>
    </aside>

    <main class="book-front">
      <div class="cover-photo" role="img" aria-label="Fotografía de un traje negro con camisa blanca y corbata roja manchada de sangre"></div>
      <h1 class="cover-text book-title">TESTIGO<br>NUEVE</h1>
      <p class="cover-text book-subtitle">EL ASESINATO DE RAMIRO ESTEBAN VALLARTA</p>
      <p class="cover-text book-author">DR. MARTÍN OLVERA QUINTANA</p>
    </main>
  </div>
</body>
</html>
```